Simple proffessional BC

I have a logo which I will attach below.
I would like the logo on the front of the card with these details in point form below:
Pre and Post Natal Yoga: Pregnancy Workshops: Hypnobirthing Courses
On the back of the card my details:
Merrin Galvey
Facebook page- calmbellieswillowharbour
Mobile- 0438 512 740

I like the idea of the card being simple, possibly just the above on a plain coloured (eggshell?) card, a card that is textured.
I am open to suggestion if it appeals!
Thank you and good luck!

Target Market(s)

Pregnant women, 20's-40's

Requirements
Must have
• Simple, compliment logo.
Make logo the feature.
Should not have

• .

```html
<!DOCTYPE html>
<html lang="en">
<head>
<meta charset="utf-8">
<title>Calm Bellies – Business Card</title>
<link href="https://fonts.googleapis.com/css2?family=Didact+Gothic&display=swap" rel="stylesheet">
<style>
  :root {
    --backdrop: #e4e4e4;
    --orange: #f29424;
    --orange-soft: #f7b25a;
    --glow: #fff1dc;
    --band: #ffffff;
    --ink: #7a1a1e;
    --mark: #eda33c;
  }
  * { box-sizing: border-box; margin: 0; padding: 0; }
  html, body {
    width: 1200px;
    height: 900px;
    overflow: hidden;
    background: var(--backdrop);
    font-family: "Didact Gothic", "Century Gothic", sans-serif;
  }
  .canvas { position: relative; width: 1200px; height: 900px; }

  .card {
    position: absolute;
    width: 560px;
    height: 340px;
    overflow: hidden;
    background:
      radial-gradient(ellipse 300px 200px at 45% 62%, var(--glow) 0%, var(--orange-soft) 45%, var(--orange) 100%);
    box-shadow: 0 6px 18px rgba(0, 0, 0, 0.12);
  }
  .card--front { left: 60px; top: 90px; }
  .card--back  { left: 580px; top: 470px; }

  .band {
    position: absolute;
    left: 0;
    width: 100%;
    background: var(--band);
  }
  .card--front .band { top: 84px; height: 104px; }
  .card--back .band  { top: 78px; height: 116px; }

  .brand {
    position: absolute;
    left: 34px;
    top: 0;
    height: 100%;
    display: flex;
    align-items: center;
    gap: 22px;
  }
  .brand__dot {
    width: 72px;
    height: 72px;
    border-radius: 50%;
    background: var(--mark);
    flex: none;
  }
  .brand__name {
    font-size: 44px;
    color: var(--ink);
    letter-spacing: 0.5px;
  }

  .services {
    position: absolute;
    left: 262px;
    top: 208px;
    list-style: none;
    color: var(--ink);
    font-size: 19px;
    line-height: 30px;
  }
  .services li::before {
    content: "•";
    margin-right: 10px;
  }

  .holder {
    position: absolute;
    left: 28px;
    bottom: 14px;
    font-size: 25px;
    color: var(--ink);
  }
  .contact {
    position: absolute;
    left: 268px;
    top: 222px;
    color: var(--ink);
    font-size: 18px;
    line-height: 36px;
  }
</style>
</head>
<body>
<main class="canvas">
  <section class="card card--front" aria-label="Card front">
    <div class="band">
      <div class="brand">
        <span class="brand__dot"></span>
        <span class="brand__name">Calm Bellies</span>
      </div>
    </div>
    <ul class="services">
      <li>Pre and Post Natal Yoga</li>
      <li>Pregnancy Workshops</li>
      <li>Hypnobirthing Courses</li>
    </ul>
  </section>

  <section class="card card--back" aria-label="Card back">
    <div class="band">
      <p class="holder">Merrin Galvey</p>
    </div>
    <div class="contact">
      <p>Fb- calmbellieswillowharbour</p>
      <p>Mobile- 0438 512 740</p>
    </div>
  </section>
</main>
</body>
</html>
```